Breezy Puffs Cotton Candy

Looking for a logo design and business cards to help a 13 year old entrepreneur promote her cotton candy business.
Contact Information for Business Card
Name, Phone & Email
Colors
E54698
E96AAD
F1A4CE
F9D9EA
FCEFF6
A7469A
B969AE
D3A5CF
EDDBEB
F8F0F9
6B429C
8869AF
B7A5CE
E3DAEB
F3F0F8
Requirements
Must have
- A fun feel that is appropriate for a teenage girl selling cotton candy

```html
<!DOCTYPE html>
<html lang="en">
<head>
<meta charset="utf-8">
<title>Breezy Puffs Cotton Candy — Business Cards</title>
<link rel="stylesheet" href="https://fonts.googleapis.com/css2?family=Montserrat:wght@400;500;700&display=swap">
<style>
  :root {
    --stage: #1c1c1e;
    --card: #0b0b0c;
    --card-edge: #161617;
    --pink: #E54698;
    --purple: #6B429C;
    --lavender: #8869AF;
    --white: #f4f4f4;
    --silver: #c9c9cc;
    --rule: #3a3a3d;
  }
  * { box-sizing: border-box; margin: 0; padding: 0; }
  html, body {
    width: 1200px; height: 900px; overflow: hidden;
    background: var(--stage);
    font-family: "Montserrat", sans-serif;
  }
  .stage {
    width: 1200px; height: 900px;
    display: flex; align-items: center; justify-content: center; gap: 40px;
  }
  .card {
    position: relative;
    width: 540px; height: 310px;
    border-radius: 22px;
    background: var(--card);
    box-shadow: 0 0 0 1px var(--card-edge), 0 18px 40px rgba(0,0,0,.55);
    overflow: hidden;
  }

  /* front */
  .brand {
    position: absolute; left: 48px; top: 72px; width: 200px;
    display: flex; flex-direction: column; align-items: flex-start; gap: 16px;
  }
  .brand-dot {
    width: 70px; height: 70px; border-radius: 50%;
    background: var(--purple);
  }
  .brand-name {
    font-weight: 700; font-size: 30px; line-height: 1.05;
    color: var(--pink); letter-spacing: -.3px;
  }
  .divider {
    position: absolute; left: 272px; top: 92px;
    width: 1px; height: 130px; background: var(--rule);
  }
  .contact { position: absolute; left: 298px; top: 104px; }
  .person-name {
    font-weight: 700; font-size: 22px; color: var(--pink); letter-spacing: .2px;
  }
  .person-title {
    font-weight: 500; font-size: 14px; color: var(--lavender); margin-top: 2px;
  }
  .details { list-style: none; margin-top: 20px; display: grid; gap: 8px; }
  .details li {
    display: flex; align-items: center; gap: 10px;
    font-size: 14px; color: var(--white);
  }
  .details svg { width: 15px; height: 15px; flex: none; }

  /* back */
  .card-back {
    display: flex; flex-direction: column; align-items: center; justify-content: center; gap: 20px;
  }
  .back-dot {
    width: 92px; height: 92px; border-radius: 50%;
    background: linear-gradient(145deg, #e6e6e8, #8f8f93);
  }
  .back-name {
    font-weight: 700; font-size: 32px; line-height: 1.05;
    color: var(--silver); text-align: center;
  }
</style>
</head>
<body>
<main class="stage">
  <section class="card card-front" aria-label="Business card front">
    <div class="brand">
      <span class="brand-dot"></span>
      <p class="brand-name">Breezy Puffs<br>Cotton Candy</p>
    </div>
    <span class="divider"></span>
    <div class="contact">
      <h1 class="person-name">Mia Carter</h1>
      <p class="person-title">Managing Director</p>
      <ul class="details">
        <li>
          <svg viewBox="0 0 24 24" aria-hidden="true"><path fill="var(--pink)" d="M6.6 10.8a15.1 15.1 0 0 0 6.6 6.6l2.2-2.2a1 1 0 0 1 1-.25 11.4 11.4 0 0 0 3.6.57 1 1 0 0 1 1 1V20a1 1 0 0 1-1 1A17 17 0 0 1 3 4a1 1 0 0 1 1-1h3.5a1 1 0 0 1 1 1c0 1.25.2 2.45.57 3.57a1 1 0 0 1-.25 1z"/></svg>
          044-555 012 345
        </li>
        <li>
          <svg viewBox="0 0 24 24" aria-hidden="true"><rect x="2" y="5" width="20" height="14" rx="1.5" fill="var(--pink)"/><path d="M3 6.5l9 6.5 9-6.5" fill="none" stroke="var(--card)" stroke-width="1.8"/></svg>
          hello@breezypuffs.com
        </li>
      </ul>
    </div>
  </section>

  <section class="card card-back" aria-label="Business card back">
    <span class="back-dot"></span>
    <p class="back-name">Breezy Puffs<br>Cotton Candy</p>
  </section>
</main>
</body>
</html>
```